Tidewell Outdoor Signage

We need an outdoor signage design for my company with new logo designed from makerhive. We do electrical, Air conditioning & Plumbing, installation, service, repairs and maintenance. The design shall be an eye catching that cannot miss ready it.

Industry/Entity Type

Electrical, Air conditioning, Plumbing

```html
<!DOCTYPE html>
<html lang="en">
<head>
<meta charset="utf-8">
<title>Tidewell Outdoor Signage</title>
<link rel="stylesheet" href="https://fonts.googleapis.com/css2?family=Montserrat:wght@600;700;800&family=Oswald:wght@500&display=swap">
<style>
  :root {
    --backdrop: #444041;
    --white: #ffffff;
    --red: #e91f29;
    --blue: #1a67b0;
    --orange: #f28b3f;
    --ink: #111111;
    --rule: #f5a03a;
  }
  * { margin: 0; padding: 0; box-sizing: border-box; }
  html, body {
    width: 1200px; height: 1200px; overflow: hidden;
    background: var(--backdrop);
  }
  .sign {
    position: absolute; left: 59px; top: 329px;
    width: 1082px; height: 541px; overflow: hidden;
  }
  .sign-bg { position: absolute; inset: 0; }
  .brand-dot {
    position: absolute; left: 190px; top: 40px;
    width: 130px; height: 130px; border-radius: 50%;
    background: var(--orange);
  }
  .brand-name {
    position: absolute; left: 40px; top: 238px;
    font-family: 'Montserrat', sans-serif; font-weight: 800;
    font-size: 96px; line-height: 1; letter-spacing: -2px;
    color: var(--orange);
  }
  .services-line {
    position: absolute; left: 42px; top: 344px;
    font-family: 'Montserrat', sans-serif; font-weight: 700;
    font-size: 23px; white-space: nowrap;
  }
  .services-line span { margin-right: 14px; }
  .services-line .electric { color: var(--red); }
  .services-line .air { color: var(--blue); }
  .services-line .plumb { color: var(--orange); }
  .phone {
    position: absolute; left: 42px; top: 374px;
    display: flex; align-items: center; gap: 8px;
  }
  .phone-number {
    font-family: 'Montserrat', sans-serif; font-weight: 800;
    font-size: 60px; line-height: 1; color: var(--red); letter-spacing: -1px;
  }
  .contact-band {
    position: absolute; left: 0; top: 444px;
    width: 507px; height: 79px; background: var(--orange);
    padding: 8px 0 0 36px;
  }
  .contact-row {
    display: flex; align-items: center; gap: 8px;
    font-family: 'Montserrat', sans-serif; font-weight: 600;
    font-size: 25px; line-height: 32px; color: var(--ink);
  }
  .service-list {
    position: absolute; left: 636px; top: 40px; width: 420px;
    list-style: none;
  }
  .service-item {
    display: flex; align-items: flex-start; gap: 22px;
    border-bottom: 2px solid var(--rule);
    padding: 6px 0 10px;
    margin-left: 0;
  }
  .service-item:last-child { border-bottom: none; }
  .service-icon { flex: 0 0 58px; height: 58px; margin-top: 6px; }
  .service-name {
    font-family: 'Oswald', sans-serif; font-weight: 500;
    font-size: 56px; line-height: 56px; color: var(--white);
    letter-spacing: -1.5px;
  }
  .service-list .service-item { position: relative; }
  .service-item::after { content: none; }
</style>
</head>
<body>
  <section class="sign">
    <svg class="sign-bg" viewBox="0 0 1082 541" width="1082" height="541" aria-hidden="true">
      <rect width="1082" height="541" fill="var(--white)"/>
      <path d="M372 6 C510 90 580 290 574 541 L594 541 C600 285 520 85 392 0 Z" fill="var(--blue)"/>
      <path d="M380 0 L1082 0 L1082 541 L617 541 C620 290 545 90 380 0 Z" fill="var(--red)"/>
    </svg>

    <div class="brand-dot" aria-hidden="true"></div>
    <div class="brand-name">Tidewell</div>
    <p class="services-line">
      <span class="electric">Electrical</span><span class="air">Air Conditioning</span><span class="plumb">Plumbing</span>
    </p>

    <div class="phone">
      <svg width="40" height="46" viewBox="0 0 40 46" aria-hidden="true">
        <path d="M8 4 L15 2 L19 13 L13 17 C15 25 19 31 25 36 L31 31 L39 39 L34 44 C20 44 4 25 4 10 Z" fill="var(--ink)"/>
        <path d="M22 10 A10 10 0 0 1 32 20 M22 4 A16 16 0 0 1 38 20" stroke="var(--ink)" stroke-width="2.5" fill="none"/>
      </svg>
      <span class="phone-number">0400 555 218</span>
    </div>

    <div class="contact-band">
      <p class="contact-row">
        <svg width="24" height="20" viewBox="0 0 24 20" aria-hidden="true"><rect x="1" y="5" width="22" height="14" fill="var(--red)"/><path d="M1 5 L12 0 L23 5 L12 13 Z" fill="var(--red)" stroke="var(--white)" stroke-width="1"/></svg>
        info@tidewellelectrical.com.au
      </p>
      <p class="contact-row">
        <svg width="24" height="24" viewBox="0 0 24 24" aria-hidden="true"><circle cx="12" cy="12" r="10" fill="none" stroke="var(--red)" stroke-width="2"/><path d="M2 12 H22 M12 2 V22 M5 6 H19 M5 18 H19" stroke="var(--red)" stroke-width="1.5"/></svg>
        www.tidewellelectrical.com.au
      </p>
    </div>

    <ul class="service-list">
      <li class="service-item">
        <svg class="service-icon" viewBox="0 0 58 58" aria-hidden="true">
          <circle cx="29" cy="29" r="26" fill="none" stroke="var(--white)" stroke-width="4"/>
          <path d="M24 20 L38 20 L38 30 C38 36 34 39 31 39 L31 46 L27 46 L27 39 C24 39 20 36 20 30 Z" fill="var(--white)"/>
          <path d="M30 24 L26 31 L30 31 L28 37 L34 28 L30 28 Z" fill="var(--red)"/>
        </svg>
        <span class="service-name">Electrical</span>
      </li>
      <li class="service-item">
        <svg class="service-icon" viewBox="0 0 58 58" aria-hidden="true">
          <g stroke="var(--white)" stroke-width="5" stroke-linecap="round">
            <path d="M29 3 V55 M6 16 L52 42 M6 42 L52 16"/>
          </g>
          <g stroke="var(--white)" stroke-width="3" fill="none" stroke-linecap="round">
            <path d="M22 8 L29 14 L36 8 M22 50 L29 44 L36 50"/>
          </g>
        </svg>
        <span class="service-name">Air conditioning<br>&amp; Plumbing</span>
      </li>
      <li class="service-item">
        <svg class="service-icon" viewBox="0 0 58 58" aria-hidden="true">
          <circle cx="27" cy="27" r="19" fill="none" stroke="var(--white)" stroke-width="9" stroke-dasharray="7 5"/>
          <circle cx="27" cy="27" r="14" fill="var(--white)"/>
          <circle cx="27" cy="27" r="8" fill="var(--red)"/>
          <path d="M30 30 L54 54" stroke="var(--white)" stroke-width="5" stroke-linecap="round"/>
        </svg>
        <span class="service-name">Installation</span>
      </li>
      <li class="service-item">
        <svg class="service-icon" viewBox="0 0 58 58" aria-hidden="true">
          <path d="M12 2 L12 10 L18 10 L18 2 C24 4 24 14 18 16 L18 30 L12 30 L12 16 C6 14 6 4 12 2 Z" fill="var(--white)"/>
          <rect x="6" y="32" width="18" height="22" rx="3" fill="var(--white)"/>
          <path d="M26 40 L36 30 L46 40 L46 54 L26 54 Z" fill="var(--white)"/>
          <rect x="48" y="38" width="8" height="16" fill="var(--white)"/>
        </svg>
        <span class="service-name">Service &amp; Repairs</span>
      </li>
      <li class="service-item">
        <svg class="service-icon" viewBox="0 0 58 58" aria-hidden="true">
          <circle cx="29" cy="18" r="13" fill="none" stroke="var(--white)" stroke-width="7" stroke-dasharray="5 4"/>
          <circle cx="29" cy="18" r="8" fill="none" stroke="var(--white)" stroke-width="4"/>
          <path d="M3 30 L10 44 L22 56 L26 56 L26 44 L16 36 M55 30 L48 44 L36 56 L32 56 L32 44 L42 36" fill="none" stroke="var(--white)" stroke-width="5" stroke-linejoin="round"/>
        </svg>
        <span class="service-name">Maintenance</span>
      </li>
    </ul>
  </section>
</body>
</html>
```